Tri-Fold Behavioral Health (Addiction) Agency Brochure

We need an updated and refreshed brochure design for our Residential Treatment Facilities. These facilities provide residential comprehensive treatment for those struggling with drug and alcohol addiction along with those who are dually diagnosed with mental health issues as well. We are starting with this brochure but plan to have our other brochures "match" the design and will submit that following completion of this design. I have attached a "Brochure Areas" document that is numbered and corresponds to the brochure areas of our current brochure. We have modified the wording in each of these areas so the wording in the attached word document is what needs to go on the design (not the words in the attached pictures of our current brochure). We want something that is a professional design look. The front page of the brochure needs to have our main agency Logo/Name: Alder Brook Behavioral Health Solutions (logo attached). The back page we would like to have the two locations listed with the address (possible map if able). The first is called: The Harbor at Alder Brook - located at 7284 Mulberry Lane, Frazeysburg OH 43815. The Second Facility is called: The Whitcomb at Alder Brook - located at 382 Kendrick St, Zanesville OH 43709. I have also attached some pictures of our facilities that can be used. They all don't have to be used and we would still like some stock photos of "people" or group counseling, etc.

Requirements
Must have
• Need final design file to be publisher or word along with pdf and or other print type file.
Nice to have
• I have also attached the current booth design photo that we are using to possibly match design look.

```html
<!DOCTYPE html>
<html lang="en">
<head>
<meta charset="utf-8">
<title>Alder Brook – Residential Treatment Inside Panel</title>
<link href="https://fonts.googleapis.com/css2?family=Raleway:wght@400;500;700;800&family=Arimo:wght@400&display=swap" rel="stylesheet">
<style>
  :root{
    --teal:#0bbec0;
    --ink:#231f20;
    --mist:#d5eced;
    --white:#ffffff;
    --photo-warm:linear-gradient(135deg,#6b4a2c 0%,#a5793f 45%,#d8b47a 100%);
    --photo-room:linear-gradient(135deg,#5a3a22 0%,#9b6b3a 50%,#e2c594 100%);
    --photo-garden:linear-gradient(160deg,#7a8f58 0%,#3f6a2e 50%,#5f8a3a 100%);
  }
  *{margin:0;padding:0;box-sizing:border-box}
  html,body{width:1200px;height:848px;overflow:hidden}
  body{background:var(--mist);position:relative;font-family:"Arimo",Arial,sans-serif}
  .abs{position:absolute}

  .band-dark{left:0;top:0;width:1200px;height:290px;background:var(--ink)}
  .panel-teal{left:0;top:329px;width:390px;height:519px;background:var(--teal)}
  .groups-box{left:887px;top:553px;width:313px;height:295px;background:var(--teal)}

  .photo{display:block}
  .photo-lounge{left:430px;top:51px;width:339px;height:231px;background:var(--photo-warm)}
  .photo-bedroom{left:810px;top:51px;width:339px;height:231px;background:var(--photo-room)}
  .photo-bar{height:8px;background:var(--teal)}
  .bar-1{left:430px;top:282px;width:339px}
  .bar-2{left:810px;top:282px;width:339px}
  .photo-parlor{left:51px;top:582px;width:339px;height:221px;background:var(--photo-warm)}
  .photo-garden{left:430px;top:553px;width:457px;height:295px;background:var(--photo-garden)}

  .num{font-family:"Raleway",sans-serif;font-weight:800;line-height:1}
  .num-1{left:48px;top:46px;font-size:56px;color:var(--teal)}
  .num-2{left:50px;top:352px;font-size:60px;color:var(--ink)}
  .num-3{left:426px;top:356px;font-size:60px;color:var(--ink)}

  .rule{height:2px}
  .rule-1{left:86px;top:51px;width:304px;background:var(--teal)}
  .rule-3a{left:430px;top:345px;width:30px;background:var(--ink)}
  .rule-3b{left:465px;top:345px;width:684px;background:var(--teal)}

  .heading{font-family:"Raleway",sans-serif;font-weight:700;font-size:24px;line-height:1;white-space:nowrap}
  .h-experience{left:88px;top:66px;color:var(--white)}
  .h-dual{left:102px;top:368px;color:var(--white);font-size:24px}
  .h-programming{left:477px;top:371px;color:var(--teal);font-size:25px}
  .h-groups{left:920px;top:567px;color:var(--white)}

  .body-copy{font-size:14px;line-height:17.1px;text-align:justify;letter-spacing:-0.35px}
  .copy-experience{left:51px;top:106px;width:339px;color:var(--white)}
  .copy-dual{left:51px;top:413px;width:308px;color:var(--white)}
  .copy-programming{left:430px;top:422px;width:339px;color:var(--ink)}

  .list{list-style:none;font-family:"Raleway",sans-serif;font-weight:500}
  .list li{display:flex;align-items:center;white-space:nowrap}
  .list svg{flex:none;margin-right:9px}
  .program-list{left:810px;top:369px;font-size:17.5px;color:var(--ink)}
  .program-list li{height:22.5px}
  .group-list{left:921px;top:606px;font-size:17px;color:var(--white)}
  .group-list li{height:24.6px}

  .nav-dot{width:28px;height:28px}
  .dot-1{left:419px;top:64px}
  .dot-2{left:795px;top:64px}
  .dot-3{left:37px;top:604px}
</style>
</head>
<body>
  <div class="abs band-dark"></div>
  <div class="abs panel-teal"></div>

  <!-- Section 1 -->
  <div class="abs num num-1">1</div>
  <div class="abs rule rule-1"></div>
  <h2 class="abs heading h-experience">The Experience</h2>
  <p class="abs body-copy copy-experience">Residential Treatment at Alder Brook offers intensive structured treatment services for men and women suffering from substance abuse disorders in a 24-hour medically monitored Long-term residential treatment facility. Our treatment facilities offer clients the ability to feel welcomed, accepted and supported in a retreat like setting. Our multi-disciplinary team consists of Physicians, Therapists, Nurses, Case Managers, and other Recovery Support Specialists, allowing for each individual’s physical, social, mental, and emotional development.</p>

  <div class="abs photo photo-lounge" role="img" aria-label="Photo of a furnished lounge with sofa, fireplace and bookshelves"></div>
  <div class="abs photo-bar bar-1"></div>
  <div class="abs photo photo-bedroom" role="img" aria-label="Photo of a bedroom with two iron-frame beds and a lamp"></div>
  <div class="abs photo-bar bar-2"></div>

  <svg class="abs nav-dot dot-1" viewBox="0 0 28 28" aria-hidden="true"><circle cx="14" cy="14" r="14" fill="var(--teal)"/><path d="M11.5 8.5 17 14l-5.5 5.5" fill="none" stroke="#fff" stroke-width="3" stroke-linecap="round" stroke-linejoin="round"/></svg>
  <svg class="abs nav-dot dot-2" viewBox="0 0 28 28" aria-hidden="true"><circle cx="14" cy="14" r="14" fill="var(--teal)"/><path d="M11.5 8.5 17 14l-5.5 5.5" fill="none" stroke="#fff" stroke-width="3" stroke-linecap="round" stroke-linejoin="round"/></svg>

  <!-- Section 2 -->
  <div class="abs num num-2">2</div>
  <h2 class="abs heading h-dual">DUAL DIAGNOSIS</h2>
  <p class="abs body-copy copy-dual">It is an unfortunate reality that many individuals who struggle with addiction are also faced with mental illness. Our residential treatment programs support dually-diagnosed individuals by providing onsite psychiatric evaluations, regular psychiatric follow-ups, medication management, and therapy services aimed at treating these symptoms as a part of the client’s individualized treatment plan.</p>
  <div class="abs photo photo-parlor" role="img" aria-label="Photo of a parlor with tufted sofas, rug and fireplace"></div>
  <svg class="abs nav-dot dot-3" viewBox="0 0 28 28" aria-hidden="true"><circle cx="14" cy="14" r="14" fill="var(--teal)"/><path d="M11.5 8.5 17 14l-5.5 5.5" fill="none" stroke="#fff" stroke-width="3" stroke-linecap="round" stroke-linejoin="round"/></svg>

  <!-- Section 3 -->
  <div class="abs rule rule-3a"></div>
  <div class="abs rule rule-3b"></div>
  <div class="abs num num-3">3</div>
  <h2 class="abs heading h-programming">Our Programming</h2>
  <p class="abs body-copy copy-programming">Residential treatment programing provides comprehensive treatment for those struggling with drug and alcohol addiction along with those who are dually diagnosed with mental health issues as well. Residents will be able to experience an evidence-based program model inclusive of:</p>

  <ul class="abs list program-list">
    <li><svg width="13" height="13" viewBox="0 0 14 14"><circle cx="7" cy="7" r="7" fill="var(--teal)"/><path d="M5.8 4.3 8.5 7l-2.7 2.7" fill="none" stroke="#fff" stroke-width="1.8" stroke-linecap="round"/></svg>Comprehensive Evaluations</li>
    <li><svg width="13" height="13" viewBox="0 0 14 14"><circle cx="7" cy="7" r="7" fill="var(--teal)"/><path d="M5.8 4.3 8.5 7l-2.7 2.7" fill="none" stroke="#fff" stroke-width="1.8" stroke-linecap="round"/></svg>Treatment Team Collaboration</li>
    <li><svg width="13" height="13" viewBox="0 0 14 14"><circle cx="7" cy="7" r="7" fill="var(--teal)"/><path d="M5.8 4.3 8.5 7l-2.7 2.7" fill="none" stroke="#fff" stroke-width="1.8" stroke-linecap="round"/></svg>Medication Management</li>
    <li><svg width="13" height="13" viewBox="0 0 14 14"><circle cx="7" cy="7" r="7" fill="var(--teal)"/><path d="M5.8 4.3 8.5 7l-2.7 2.7" fill="none" stroke="#fff" stroke-width="1.8" stroke-linecap="round"/></svg>Aftercare Planning</li>
    <li><svg width="13" height="13" viewBox="0 0 14 14"><circle cx="7" cy="7" r="7" fill="var(--teal)"/><path d="M5.8 4.3 8.5 7l-2.7 2.7" fill="none" stroke="#fff" stroke-width="1.8" stroke-linecap="round"/></svg>Individual Therapy</li>
    <li><svg width="13" height="13" viewBox="0 0 14 14"><circle cx="7" cy="7" r="7" fill="var(--teal)"/><path d="M5.8 4.3 8.5 7l-2.7 2.7" fill="none" stroke="#fff" stroke-width="1.8" stroke-linecap="round"/></svg>Family Therapy</li>
    <li><svg width="13" height="13" viewBox="0 0 14 14"><circle cx="7" cy="7" r="7" fill="var(--teal)"/><path d="M5.8 4.3 8.5 7l-2.7 2.7" fill="none" stroke="#fff" stroke-width="1.8" stroke-linecap="round"/></svg>Group Therapy</li>
  </ul>

  <div class="abs photo photo-garden" role="img" aria-label="Photo of the facility garden with sunroom, steps, shrubs and a stone statue"></div>

  <div class="abs groups-box"></div>
  <h2 class="abs heading h-groups">Groups</h2>
  <ul class="abs list group-list">
    <li><svg width="13" height="13" viewBox="0 0 14 14"><circle cx="7" cy="7" r="7" fill="var(--ink)"/><path d="M5.8 4.3 8.5 7l-2.7 2.7" fill="none" stroke="#fff" stroke-width="1.8" stroke-linecap="round"/></svg>Psychoeducational</li>
    <li><svg width="13" height="13" viewBox="0 0 14 14"><circle cx="7" cy="7" r="7" fill="var(--ink)"/><path d="M5.8 4.3 8.5 7l-2.7 2.7" fill="none" stroke="#fff" stroke-width="1.8" stroke-linecap="round"/></svg>Psychotherapy</li>
    <li><svg width="13" height="13" viewBox="0 0 14 14"><circle cx="7" cy="7" r="7" fill="var(--ink)"/><path d="M5.8 4.3 8.5 7l-2.7 2.7" fill="none" stroke="#fff" stroke-width="1.8" stroke-linecap="round"/></svg>Health &amp; Wellness</li>
    <li><svg width="13" height="13" viewBox="0 0 14 14"><circle cx="7" cy="7" r="7" fill="var(--ink)"/><path d="M5.8 4.3 8.5 7l-2.7 2.7" fill="none" stroke="#fff" stroke-width="1.8" stroke-linecap="round"/></svg>Independent Living Skills</li>
    <li><svg width="13" height="13" viewBox="0 0 14 14"><circle cx="7" cy="7" r="7" fill="var(--ink)"/><path d="M5.8 4.3 8.5 7l-2.7 2.7" fill="none" stroke="#fff" stroke-width="1.8" stroke-linecap="round"/></svg>Peer-Led (AA/NA)</li>
    <li><svg width="13" height="13" viewBox="0 0 14 14"><circle cx="7" cy="7" r="7" fill="var(--ink)"/><path d="M5.8 4.3 8.5 7l-2.7 2.7" fill="none" stroke="#fff" stroke-width="1.8" stroke-linecap="round"/></svg>Grief &amp; Loss</li>
    <li><svg width="13" height="13" viewBox="0 0 14 14"><circle cx="7" cy="7" r="7" fill="var(--ink)"/><path d="M5.8 4.3 8.5 7l-2.7 2.7" fill="none" stroke="#fff" stroke-width="1.8" stroke-linecap="round"/></svg>Codependency</li>
    <li><svg width="13" height="13" viewBox="0 0 14 14"><circle cx="7" cy="7" r="7" fill="var(--ink)"/><path d="M5.8 4.3 8.5 7l-2.7 2.7" fill="none" stroke="#fff" stroke-width="1.8" stroke-linecap="round"/></svg>Stress Management</li>
  </ul>
</body>
</html>
```